Investment Memorandum Document

IM for Harbourline Lending Fund - is the document that needs work

Make sure it is all done in MS WORD so that i or lawyers can edit some words if required

the IM is NOT final but its 95% of the way there. Maybe a few more pages and wording changes - but that is something i can do i guess or you can easier adjust

Just to typeset and pretty it all up - a few sample finished products have been uploaded for reference.

KPT IM is the one i like - but feel free to show off your skills

put 1.2 to 1.8 all in contrasting row tables

Target Market(s)

Individual and Institutional investors with money

Industry/Entity Type

Investment Banking

Colors

Designer to choose colors to be used in the design.

Requirements
Must have
• clear professional layout and easy on the eye
• https://www.filebarn-example.net/sh/84m7t55xqk2wbnr/QQzdLeMu8RplbqTYAXNW47Ko?dl=0
• use the link above for high res images
Nice to have
• pictures and graphics
Should not have
• cartoons

```html
<!DOCTYPE html>
<html lang="en">
<head>
<meta charset="utf-8">
<title>Harbourline – Information Memorandum Cover Styles</title>
<link href="https://fonts.googleapis.com/css2?family=Arimo:wght@400;700&family=Open+Sans:ital,wght@1,300&display=swap" rel="stylesheet">
<style>
  :root{
    --board:#d8d8d8;
    --caption:#3a3a3a;
    --white:#ffffff;
    --gold:#c9953a;
    --gold-soft:rgba(214,166,84,.72);
    --gold-light:rgba(240,205,140,.72);
    --blue-deep:#173a6e;
    --blue-mid:#3f6fae;
    --blue-light:#9fc0e6;
    --blue-veil:rgba(150,180,220,.6);
  }
  *{margin:0;padding:0;box-sizing:border-box}
  html,body{width:1200px;height:1000px;overflow:hidden;background:var(--board)}
  .board{position:relative;width:1200px;height:1000px;font-family:"Arimo",Arial,sans-serif}
  .cover{position:absolute;width:368px;height:514px;overflow:hidden;box-shadow:0 14px 30px rgba(0,0,0,.35)}
  .cover--gold-tower{left:30px;top:242px}
  .cover--blue-glass{left:420px;top:236px}
  .cover--gold-glass{left:810px;top:236px}
  .cover__art{position:absolute;inset:0;width:100%;height:100%}
  .brand{position:absolute;left:48px;top:58px;display:flex;align-items:center;gap:10px;color:var(--white)}
  .brand__mark{width:26px;height:26px;border:2px solid var(--white)}
  .brand__name{font-size:29px;letter-spacing:3px;line-height:1;border-left:1px solid var(--white);padding-left:8px}
  .brand__name small{display:block;font-size:8px;letter-spacing:3.2px;margin-top:3px}
  .cover__title{position:absolute;left:45px;top:132px;color:var(--white);font-weight:700;font-size:13.5px;line-height:17px}
  .parties{position:absolute;right:22px;bottom:52px;text-align:right;color:var(--white)}
  .cover--gold-tower .parties{right:40px;bottom:40px}
  .parties__role{font-weight:700;font-size:13px;line-height:15px}
  .parties__name{font-size:10.5px;line-height:13px;margin-bottom:12px}
  .parties__name--small{font-size:7.6px;margin-bottom:0}
  .caption{position:absolute;left:0;right:0;top:862px;text-align:center;font-family:"Open Sans",Arial,sans-serif;font-style:italic;font-weight:300;font-size:30px;color:var(--caption)}
</style>
</head>
<body>
<main class="board">

  <section class="cover cover--gold-tower">
    <svg class="cover__art" viewBox="0 0 368 514" preserveAspectRatio="none">
      <defs>
        <linearGradient id="photoGoldTower" x1="0" y1="0" x2="1" y2="1">
          <stop offset="0" stop-color="#c8a25a"/><stop offset=".5" stop-color="#8a9ab0"/><stop offset="1" stop-color="#2e4f7a"/>
        </linearGradient>
      </defs>
      <rect width="368" height="514" fill="url(#photoGoldTower)" role="img" aria-label="Photograph of curved office towers with glass facades reflecting the sky"/>
      <polygon points="0,0 340,0 368,40 368,60 250,170 0,170" fill="var(--gold-soft)"/>
      <polygon points="0,170 250,170 0,430" fill="var(--gold-light)"/>
      <polygon points="170,392 368,392 368,514 60,514" fill="var(--gold-soft)"/>
      <rect x="342" y="0" width="26" height="514" fill="var(--gold)" opacity=".55"/>
    </svg>
    <div class="brand"><span class="brand__mark"></span><span class="brand__name">HARBOURLINE<small>ASSET MANAGEMENT</small></span></div>
    <h1 class="cover__title">Diversified Commercial Income Fund<br>Information Memorandum</h1>
    <div class="parties">
      <p class="parties__role">Investment Manager</p>
      <p class="parties__name">Harbourline Asset Management Pty Ltd</p>
      <p class="parties__role">Trustee</p>
      <p class="parties__name parties__name--small">Kestrel Investments and Lending Corporation Pty Ltd</p>
    </div>
  </section>

  <section class="cover cover--blue-glass">
    <svg class="cover__art" viewBox="0 0 368 514" preserveAspectRatio="none">
      <defs>
        <linearGradient id="photoBlueGlass" x1="0" y1="0" x2="1" y2="1">
          <stop offset="0" stop-color="var(--blue-light)"/><stop offset=".45" stop-color="var(--blue-mid)"/><stop offset="1" stop-color="var(--blue-deep)"/>
        </linearGradient>
      </defs>
      <rect width="368" height="514" fill="url(#photoBlueGlass)" role="img" aria-label="Photograph looking up at blue glass skyscrapers"/>
      <polygon points="0,0 345,0 240,172 0,172" fill="var(--blue-veil)"/>
      <rect x="344" y="0" width="24" height="514" fill="var(--blue-mid)" opacity=".55"/>
    </svg>
    <div class="brand"><span class="brand__mark"></span><span class="brand__name">HARBOURLINE<small>ASSET MANAGEMENT</small></span></div>
    <h1 class="cover__title">Diversified Commercial Income Fund<br>Information Memorandum</h1>
    <div class="parties">
      <p class="parties__role">Investment Manager</p>
      <p class="parties__name">Harbourline Asset Management Pty Ltd</p>
      <p class="parties__role">Trustee</p>
      <p class="parties__name parties__name--small">Kestrel Investments and Lending Corporation Pty Ltd</p>
    </div>
  </section>

  <section class="cover cover--gold-glass">
    <svg class="cover__art" viewBox="0 0 368 514" preserveAspectRatio="none">
      <defs>
        <linearGradient id="photoGoldGlass" x1="0" y1="0" x2="1" y2="1">
          <stop offset="0" stop-color="#b9cde6"/><stop offset=".45" stop-color="var(--blue-mid)"/><stop offset="1" stop-color="var(--blue-deep)"/>
        </linearGradient>
      </defs>
      <rect width="368" height="514" fill="url(#photoGoldGlass)" role="img" aria-label="Photograph looking up at blue glass skyscrapers"/>
      <polygon points="0,0 345,0 240,172 0,172" fill="var(--gold-light)"/>
      <polygon points="250,0 345,0 368,40 368,140 220,300" fill="var(--gold-soft)" opacity=".7"/>
      <rect x="344" y="0" width="24" height="514" fill="var(--gold)" opacity=".8"/>
    </svg>
    <div class="brand"><span class="brand__mark"></span><span class="brand__name">HARBOURLINE<small>ASSET MANAGEMENT</small></span></div>
    <h1 class="cover__title">Diversified Commercial Income Fund<br>Information Memorandum</h1>
    <div class="parties">
      <p class="parties__role">Investment Manager</p>
      <p class="parties__name">Harbourline Asset Management Pty Ltd</p>
      <p class="parties__role">Trustee</p>
      <p class="parties__name parties__name--small">Kestrel Investments and Lending Corporation Pty Ltd</p>
    </div>
  </section>

  <p class="caption">3 different style cover page</p>
</main>
</body>
</html>
```